Drinking Water Protection Postcard Series

Design a series of 3 themed postcards that will be mailed in succession for a pilot project. Audience: to reach water operators who are responsible for managing very small public water systems (serving less than 1000 people in Pennsylvania). Purpose: Encourage small water systems to enter into a voluntary program known as "Brightmere Wellhead Care for Hamlet Utilities" that is available at no out of pocket cost from Harlow Bureau of Habitat Stewardship (HBHS). Source Water Protection helps protect public health by preventing contaminants from entering the rivers, streams and groundwater on which the public depends for source of drinking water. Source water protection safeguards public health, makes efficient use of limited financial resources (prevention is cheaper than water treatment or loss of a well), and has a positive impact on the environment as a whole. Slogan is: "Safe Drinking Water Starts at the Source." A Source Water Protection program maps out where your drinking water comes from, shows ways to stop pollution before it starts, and helps plan for water emergencies.
We have a logo for the program (and more info) that can be seen at www.brightmerewellhead.example.org and is attached. We are considering a tag line like: "Show you care. Get a Source Water Protection Plan for your water system." Would like to see designs that use the colors blue and green, and families, a glass of water to communicate good stewardship is smart business. Many small water systems are privately owned mobile home parks.
Reason: Some designers emailed they were going to submit, but I don't believe we received their designs yet. Thank you all for your work.
Sorry for the delay in responding. 9/30 was year end for us which took priority over our new projects. We are getting back on track and have sent designs out for review and input from our small nonprofit team. Thanks for your patience, and if you have had any other inspirations that may encourage water systems to protect their raw drinking water sources out in the watershed, please send them along; we will be reviewing this week. Preventing pollution up front is much cheaper and safer than trying to treat for every contaminant at the water treatment plant. Many thanks.
about 95% mail blue collar adults; aged 25 - 65 in more rural areas of Pennsylvania.
Water Treatment

```html
<!DOCTYPE html>
<html lang="en">
<head>
<meta charset="utf-8">
<title>Brightmere Wellhead Care – Postcard</title>
<link href="https://fonts.googleapis.com/css2?family=Teko:wght@500;600&family=Lato:wght@400;700&family=Roboto+Condensed:wght@400;700&family=Tinos:wght@700&display=swap" rel="stylesheet">
<style>
  :root{
    --page:#e6e9ee;
    --navy:#1d2f6b;
    --deep:#1e4f9e;
    --royal:#2a66b8;
    --sky:#2ba6e0;
    --teal:#1aa3b5;
    --pale:#e4f1fb;
    --ink:#2a2f3a;
    --white:#ffffff;
  }
  *{box-sizing:border-box;margin:0;padding:0}
  html,body{width:877px;height:1200px;overflow:hidden;background:var(--page)}
  .canvas{position:relative;width:877px;height:1200px}

  .card{position:absolute;left:55px;width:767px;height:500px;overflow:hidden;background:var(--white);box-shadow:0 2px 6px rgba(0,0,0,.18)}
  .card--front{top:60px;background:linear-gradient(180deg,#ffffff 0%,var(--pale) 55%,#d3e8f7 100%)}
  .card--back{top:630px}
  .card svg.bg{position:absolute;inset:0}

  .brand{position:absolute;left:30px;top:200px;width:200px;display:flex;align-items:center;gap:10px}
  .brand__dot{flex:none;width:30px;height:30px;border-radius:50%;background:var(--royal)}
  .brand__name{font:700 17px/1.15 Lato,sans-serif;color:var(--navy)}

  .headline{position:absolute;right:22px;top:118px;text-align:right;font-family:Teko,sans-serif;font-weight:600;text-transform:uppercase;line-height:.9}
  .headline__top{display:block;font-size:47px;color:var(--sky)}
  .headline__bottom{display:block;font-size:60px;color:#1b8fd6}
  .tagline{position:absolute;right:22px;top:278px;text-align:right;font:700 18px/1.3 Lato,sans-serif;color:var(--navy)}

  .splash{position:absolute;left:0;bottom:0;width:767px;height:190px}

  .info{position:absolute;left:0;top:0;width:395px;height:500px;background:linear-gradient(180deg,#fff 30%,#eef1f5 100%)}
  .info__title{position:absolute;left:30px;top:62px;font:400 15.5px/1.2 "Roboto Condensed",sans-serif;color:var(--teal)}
  .info__lead{position:absolute;left:30px;top:84px;width:360px;font:700 14.5px/1.4 Tinos,serif;color:var(--navy)}
  .info__icon{position:absolute;left:181px;top:130px;width:36px;height:36px;border-radius:50%;border:2px solid var(--navy);background:#fff;display:flex;align-items:center;justify-content:center}
  .benefits__title{position:absolute;left:0;width:395px;top:180px;text-align:center;font:600 25px/1 Teko,sans-serif;color:var(--teal)}
  .benefits{position:absolute;left:30px;top:210px;width:355px;list-style:none}
  .benefits li{position:relative;padding-left:20px;margin-bottom:7px;font:400 11px/1.3 Lato,sans-serif;color:var(--ink)}
  .benefits li svg{position:absolute;left:0;top:1px}

  .contact{position:absolute;left:0;bottom:0;width:395px;height:148px;color:#fff}
  .contact svg{position:absolute;inset:0}
  .contact__intro{position:absolute;left:30px;top:34px;font:400 13px/1.3 "Roboto Condensed",sans-serif}
  .regions{position:absolute;left:30px;top:74px;display:grid;grid-template-columns:180px 180px;row-gap:8px;font:400 10px/1.2 "Roboto Condensed",sans-serif;color:#fff}
  .regions b{font-weight:400;color:#6fd0ef}

  .address{position:absolute;left:395px;top:0;width:372px;height:500px;background:#fff}
  .stamp{position:absolute;right:25px;top:24px;width:74px;height:90px;border:1.5px solid #222}
  .address__line{position:absolute;left:90px;width:270px;border-top:1.5px solid #222}
</style>
</head>
<body>
<main class="canvas">

  <section class="card card--front" aria-label="Postcard front">
    <svg class="bg" width="767" height="500" viewBox="0 0 767 500">
      <path d="M0 0H767V45C560 60 360 60 190 90C100 105 40 130 0 160Z" fill="var(--deep)"/>
      <path d="M0 160C40 130 100 105 190 90C360 60 560 60 767 45V62C560 78 360 80 200 104C110 118 45 140 0 172Z" fill="#bfe3f5"/>
      <path d="M160 88C360 56 560 52 767 40V48C560 62 360 66 170 96Z" fill="var(--sky)"/>
    </svg>

    <div class="brand">
      <span class="brand__dot"></span>
      <span class="brand__name">Brightmere Wellhead Care</span>
    </div>

    <h1 class="headline">
      <span class="headline__top">Brightmere Wellhead Care</span>
      <span class="headline__bottom">For Hamlet Utilities</span>
    </h1>
    <p class="tagline">Protect the economic future of your community<br>by protecting your water supply</p>

    <svg class="splash" viewBox="0 0 767 190" role="img" aria-label="Splash of clear blue water with bubbles flowing across the card">
      <defs>
        <linearGradient id="waterFlow" x1="0" y1="0" x2="1" y2="0">
          <stop offset="0" stop-color="#2a66b8"/>
          <stop offset=".5" stop-color="#7fc4ec"/>
          <stop offset="1" stop-color="#2a66b8"/>
        </linearGradient>
      </defs>
      <path d="M0 80C120 140 240 170 380 140C520 110 640 40 767 30V190H0Z" fill="#cfe6f6"/>
      <path d="M0 110C130 160 260 180 400 150C530 122 650 70 767 62V110C650 120 540 170 400 182C250 194 120 170 0 140Z" fill="url(#waterFlow)" opacity=".85"/>
    </svg>
  </section>

  <section class="card card--back" aria-label="Postcard back">
    <div class="info">
      <svg class="bg" width="395" height="500" viewBox="0 0 395 500">
        <path d="M0 0H395V30C300 20 180 28 90 40C50 46 20 52 0 58Z" fill="var(--deep)"/>
        <path d="M0 58C20 52 50 46 90 40C180 28 300 20 395 30V40C300 32 180 38 90 50C50 55 20 60 0 66Z" fill="var(--sky)"/>
      </svg>

      <h2 class="info__title">Brightmere Wellhead Care for Hamlet Utilities :</h2>
      <p class="info__lead">A voluntary program available at no out-of-pocket cost from Harlow Bureau of Habitat Stewardship (HBHS)</p>
      <span class="info__icon">
        <svg width="16" height="20" viewBox="0 0 16 20"><path d="M2 2H14L12 18H4Z" fill="none" stroke="var(--navy)" stroke-width="1.6"/><path d="M3.5 8H12.5L11.5 16.5H4.5Z" fill="var(--sky)"/></svg>
      </span>

      <h3 class="benefits__title">Benefits :</h3>
      <ul class="benefits">
        <li><svg width="9" height="12" viewBox="0 0 9 12"><path d="M4.5 0C6 3 9 6 9 8A4.5 4 0 0 1 0 8C0 6 3 3 4.5 0Z" fill="var(--royal)"/></svg>Includes a map showing the source water area for your well(s) and where possible pollution threats are located.</li>
        <li><svg width="9" height="12" viewBox="0 0 9 12"><path d="M4.5 0C6 3 9 6 9 8A4.5 4 0 0 1 0 8C0 6 3 3 4.5 0Z" fill="var(--royal)"/></svg>Identifies the steps needed to help prevent threats to your water system.</li>
        <li><svg width="9" height="12" viewBox="0 0 9 12"><path d="M4.5 0C6 3 9 6 9 8A4.5 4 0 0 1 0 8C0 6 3 3 4.5 0Z" fill="var(--royal)"/></svg>Provides a contingency plan to help deal with water emergencies.</li>
        <li><svg width="9" height="12" viewBox="0 0 9 12"><path d="M4.5 0C6 3 9 6 9 8A4.5 4 0 0 1 0 8C0 6 3 3 4.5 0Z" fill="var(--royal)"/></svg>Gives you a management tool that can sustain your water supply, reduce water treatment costs, ward off pollution and protect public health.</li>
      </ul>

      <div class="contact">
        <svg width="395" height="148" viewBox="0 0 395 148">
          <path d="M0 14C120 -4 260 -2 395 16V148H0Z" fill="var(--deep)"/>
          <path d="M0 8C120 -10 260 -8 395 10V18C260 2 120 0 0 18Z" fill="var(--sky)"/>
        </svg>
        <p class="contact__intro">To Learn More, contact the<br>HBHS Wellhead Care Coordinator for your region:</p>
        <div class="regions">
          <span><b>HBHS Northwest Region</b> - 555-210-0141</span>
          <span><b>HBHS Northcentral Region</b> - 555-210-0162</span>
          <span><b>HBHS Southwest Region</b> - 555-210-0173</span>
          <span><b>HBHS Southcentral Region</b> - 555-210-0184</span>
          <span><b>HBHS Northeast Region</b> - 555-210-0195</span>
          <span><b>HBHS Southeast Region</b> - 555 210-0126</span>
        </div>
      </div>
    </div>

    <div class="address">
      <div class="stamp"></div>
      <div class="address__line" style="top:255px"></div>
      <div class="address__line" style="top:312px"></div>
      <div class="address__line" style="top:368px"></div>
    </div>
  </section>

</main>
</body>
</html>
```